DL size flyer for Autism Consultancy website

We need a printed flyer DL size ( 210mmx99mm) for our Autism Consultancy website www.brightpathkids.nz which provides therapy for autistic children.
I want the flyer to look consistent with the website’s design. Please feel free to use the colour scheme, fonts, icons or any images from www.brightpathkids.nz.It should be easy to see “Autism” or “Autistic” word from a distance.
Please use either an oversized logo or make “Do you have a verbal and able autistic child?” more prominent.
Please do not convert the text fields to outlines, i.e. I need to be able to edit any text after.The final design should be either in Adobe Illustrator or Adobe Photoshop format.
The Specs for the flyer are
Document Trim Size99 x 210 mm 1169 x 2480 pixels
Full Bleed Size102 x 213 mm 1205 x 2516 pixels
Our Logo https://1drv.ms/u/s!AoH0rRjDY2GYg6QtU-xjoVlmslKp6gPlease
use this photo for the front side https://qzdropbin.io/f/Pw4KcN8rTyH2mXs6BvLd9QeFz1Gj
another one for reverse
https://qzdropbin.io/f/Rk2HsV5nWqJ7tZc3MfXb8LpYd4Ne
Please use the following content:
Do you have a verbal and able autistic child?
We use child-centred, modern and innovative approaches
Teaching autistic children to bond, laugh and play.
We work with schools
We help autistic children to develop social minds
We offer:
• Specialist assessments
• Consultations for parents & schools
• Social learning programmes
• Social-cognitive therapy
We can create an individual learning path, best suited for your child.
Our programmes and interventions include:
• Chatter Quest
• Peer Bright
• Team Puzzles
• Tingle Words
• Pebble Tales
• Pembrook Speech Ladder
• Vorlin Method
• BRIMLE Method
• Tandem Pattern Coaching
contact details on both sides:
www.brightpathkids.nz
info@brightpathkids.nz
(09) 57-318-46

```html
<!DOCTYPE html>
<html lang="en">
<head>
<meta charset="utf-8">
<title>Bright Path Kids Consultancy – DL Flyer</title>
<link rel="stylesheet" href="https://fonts.googleapis.com/css2?family=Share+Tech&family=Mulish:wght@400;500&display=swap">
<style>
:root{
  --navy:#1b2a5c;
  --teal:#45c8c0;
  --yellow:#fdd326;
  --band-grey:#eeeff0;
  --page:#d3d3d3;
  --white:#ffffff;
  --body-text:#3a4150;
}
*{box-sizing:border-box;margin:0;padding:0}
html,body{width:1200px;height:1200px;overflow:hidden;background:var(--page)}
.canvas{position:relative;width:1200px;height:1200px}
.flyer{position:absolute;top:206px;width:371px;height:787px;background:var(--white);overflow:hidden;font-family:"Mulish",sans-serif;color:var(--body-text)}
.flyer--front{left:185px}
.flyer--back{left:644px}
.display{font-family:"Share Tech",sans-serif;color:var(--navy)}
.brand{position:absolute;left:0;right:0;display:flex;align-items:center;justify-content:center;gap:9px}
.brand__dot{width:14px;height:14px;border-radius:50%;background:var(--yellow)}
.brand__name{font-family:"Share Tech",sans-serif;color:var(--navy);font-size:22px;line-height:1}
.photo{position:absolute}
.panel{position:absolute}
.tick{width:10px;height:10px;flex:none;margin-top:2px}
.list{position:absolute;list-style:none;display:flex;flex-direction:column}
.list li{display:flex;gap:7px;font-size:10.5px;line-height:13.5px}
/* front */
.front-brand{top:52px}
.front-photo{left:0;top:112px;width:309px;height:282px;background:linear-gradient(120deg,#c98a5e 0%,#efe3d6 40%,#f4ead8 60%,#8fa6c4 100%)}
.front-strip{left:309px;top:112px;width:62px;height:282px;background:var(--teal)}
.headline-band{position:absolute;left:0;top:394px;width:371px;height:82px;background:var(--band-grey);text-align:center;padding-top:13px}
.headline{font-size:22px;line-height:28px;letter-spacing:.5px}
.list--left{left:30px;top:502px;gap:12px;width:150px}
.list--right{left:197px;top:502px;gap:12px;width:160px}
.offer-teal{left:0;top:618px;width:79px;height:96px;background:var(--teal)}
.offer-yellow{left:85px;top:618px;width:286px;height:96px;background:var(--yellow)}
.offer-title{position:absolute;left:110px;top:626px;font-size:16px}
.list--offer-a{left:112px;top:651px;gap:10px;width:110px}
.list--offer-b{left:229px;top:651px;gap:10px;width:120px}
.list--offer-a li,.list--offer-b li{font-size:10px;line-height:12.5px;color:#4a4a3a}
.call{position:absolute;left:50%;transform:translateX(-50%);background:var(--navy);color:var(--white);font-family:"Share Tech",sans-serif;font-size:12.5px;letter-spacing:.6px;padding:3px 10px;border-radius:10px;white-space:nowrap}
.contact{position:absolute;left:0;right:0;display:flex;justify-content:center;gap:12px;font-family:"Share Tech",sans-serif;font-size:9.5px;color:var(--navy)}
.contact span{display:flex;align-items:center;gap:4px}
.contact svg{width:10px;height:10px}
/* back */
.back-banner{position:absolute;left:0;top:10px;width:371px;height:64px;background:var(--yellow);text-align:center;padding-top:12px}
.back-banner p{font-size:18px;line-height:22px;letter-spacing:.4px}
.back-strip{left:0;top:80px;width:80px;height:351px;background:var(--teal)}
.back-photo{left:80px;top:80px;width:291px;height:351px;background:linear-gradient(135deg,#e8c9a0 0%,#d9b48a 45%,#e9d3b6 70%,#d64a4a 100%)}
.programmes-title{position:absolute;left:30px;top:472px;font-size:15px}
.programmes-title em{font-style:normal;color:var(--teal)}
.list--prog-a{left:30px;top:508px;gap:8.5px}
.list--prog-b{left:158px;top:508px;gap:8.5px}
.list--prog-a li,.list--prog-b li{font-size:11px;line-height:13px}
.back-brand{top:662px}
.back-footer{position:absolute;left:0;top:738px;width:371px;height:49px;background:var(--teal)}
</style>
</head>
<body>
<svg width="0" height="0" style="position:absolute" aria-hidden="true">
  <symbol id="tick" viewBox="0 0 10 10"><circle cx="5" cy="5" r="4.2" fill="none" stroke="currentColor" stroke-width="1"/><path d="M3 5.2l1.4 1.4L7.2 3.6" fill="none" stroke="currentColor" stroke-width="1"/></symbol>
  <symbol id="mail" viewBox="0 0 10 10"><rect x="1" y="2.5" width="8" height="5.5" fill="none" stroke="currentColor" stroke-width=".9"/><path d="M1 2.5l4 3 4-3" fill="none" stroke="currentColor" stroke-width=".9"/></symbol>
  <symbol id="globe" viewBox="0 0 10 10"><circle cx="5" cy="5" r="3.8" fill="none" stroke="currentColor" stroke-width=".9"/><path d="M1.2 5h7.6M5 1.2c-2 2.4-2 5.2 0 7.6M5 1.2c2 2.4 2 5.2 0 7.6" fill="none" stroke="currentColor" stroke-width=".8"/></symbol>
</svg>
<main class="canvas">
  <section class="flyer flyer--front">
    <div class="brand front-brand"><span class="brand__dot"></span><span class="brand__name">Bright Path Kids Consultancy</span></div>
    <div class="photo front-photo" role="img" aria-label="Photo: a smiling boy holding a teddy bear sits facing a therapist in a bright playroom"></div>
    <div class="panel front-strip"></div>
    <div class="headline-band"><h1 class="display headline">Do you have a<br>verbal and able autistic child?</h1></div>
    <ul class="list list--left" style="color:var(--navy)">
      <li><svg class="tick"><use href="#tick"/></svg><span style="color:var(--body-text)">We use child-centred, modern and innovative approaches</span></li>
      <li><svg class="tick"><use href="#tick"/></svg><span style="color:var(--body-text)">Teaching autistic children to bond, laugh and play.</span></li>
    </ul>
    <ul class="list list--right" style="color:var(--navy)">
      <li><svg class="tick"><use href="#tick"/></svg><span style="color:var(--body-text)">We work with schools</span></li>
      <li><svg class="tick"><use href="#tick"/></svg><span style="color:var(--body-text)">We help autistic children to develop social minds</span></li>
    </ul>
    <div class="panel offer-teal"></div>
    <div class="panel offer-yellow"></div>
    <h2 class="display offer-title">We offer:</h2>
    <ul class="list list--offer-a">
      <li><svg class="tick"><use href="#tick"/></svg><span>Specialist assessments</span></li>
      <li><svg class="tick"><use href="#tick"/></svg><span>Consultations for parents &amp; schools</span></li>
    </ul>
    <ul class="list list--offer-b">
      <li><svg class="tick"><use href="#tick"/></svg><span>Social learning programmes</span></li>
      <li><svg class="tick"><use href="#tick"/></svg><span>Social-cognitive therapy</span></li>
    </ul>
    <div class="call" style="top:727px">call us now (09) 57-318-46</div>
    <div class="contact" style="top:757px"><span><svg><use href="#mail"/></svg>info@brightpathkids.nz</span><span><svg><use href="#globe"/></svg>www.brightpathkids.nz</span></div>
  </section>

  <section class="flyer flyer--back">
    <div class="back-banner"><p class="display">We can create an individual learning path,<br>best suited for your child.</p></div>
    <div class="panel back-strip"></div>
    <div class="photo back-photo" role="img" aria-label="Photo: a boy in a striped top lies on a wooden floor playing among scattered toy cars"></div>
    <h2 class="display programmes-title">Our programmes and <em>interventions include:</em></h2>
    <ul class="list list--prog-a" style="color:var(--navy)">
      <li><svg class="tick"><use href="#tick"/></svg><span style="color:var(--body-text)">Chatter Quest</span></li>
      <li><svg class="tick"><use href="#tick"/></svg><span style="color:var(--body-text)">Peer Bright</span></li>
      <li><svg class="tick"><use href="#tick"/></svg><span style="color:var(--body-text)">Team Puzzles</span></li>
      <li><svg class="tick"><use href="#tick"/></svg><span style="color:var(--body-text)">Tingle Words</span></li>
      <li><svg class="tick"><use href="#tick"/></svg><span style="color:var(--body-text)">Pebble Tales</span></li>
    </ul>
    <ul class="list list--prog-b" style="color:var(--navy)">
      <li><svg class="tick"><use href="#tick"/></svg><span style="color:var(--body-text)">Pembrook Speech Ladder</span></li>
      <li><svg class="tick"><use href="#tick"/></svg><span style="color:var(--body-text)">Vorlin Method</span></li>
      <li><svg class="tick"><use href="#tick"/></svg><span style="color:var(--body-text)">BRIMLE Method</span></li>
      <li><svg class="tick"><use href="#tick"/></svg><span style="color:var(--body-text)">Tandem Pattern Coaching</span></li>
    </ul>
    <div class="brand back-brand"><span class="brand__dot"></span><span class="brand__name" style="font-size:19px">Bright Path Kids Consultancy</span></div>
    <div class="back-footer"></div>
    <div class="call" style="top:728px">call us now (09) 57-318-46</div>
    <div class="contact" style="top:757px"><span><svg><use href="#mail"/></svg>info@brightpathkids.nz</span><span><svg><use href="#globe"/></svg>www.brightpathkids.nz</span></div>
  </section>
</main>
</body>
</html>
```